Business Card Design Project

looking for business cards with new logo

I am looking to keep with the colors of the logo i posted.  Here are some other details to consider.  I would like my website prominently displayed on the business card with the logo.  my website is www.HavenrockTX.com...it should be spelled this way.

My contact information is:

Daniel P Whitcomb III
Broker/Owner
48391 Cordell Ave., Suite 307
Calderon, Texas 78115
Office: 210-555-0147
Email:  Daniel@HavenrockTX.com

Thank you
Daniel Whitcomb

```html
<!DOCTYPE html>
<html lang="en">
<head>
<meta charset="utf-8">
<title>Havenrock Realty – Business Card</title>
<link href="https://fonts.googleapis.com/css2?family=Josefin+Sans:wght@400;500;600;700&display=swap" rel="stylesheet">
<style>
  :root {
    --navy: #0d2b8f;
    --cyan: #52d6f2;
    --white: #ffffff;
    --paper: #ffffff;
  }
  html, body {
    margin: 0;
    padding: 0;
    overflow: hidden;
    background: var(--paper);
  }
  .card {
    position: relative;
    width: 685px;
    height: 1200px;
    overflow: hidden;
    background: var(--paper);
    font-family: "Josefin Sans", sans-serif;
    color: var(--white);
  }
  .card__disc {
    position: absolute;
    inset: 0;
  }
  .line {
    position: absolute;
    left: 0;
    width: 685px;
    margin: 0;
    text-align: center;
    line-height: 1;
    white-space: nowrap;
  }
  .brand__name {
    top: 258px;
    font-size: 118px;
    font-weight: 500;
    letter-spacing: -1px;
  }
  .brand__tagline {
    top: 383px;
    font-size: 36px;
    font-weight: 500;
    letter-spacing: 14px;
    padding-left: 14px;
    box-sizing: border-box;
  }
  .rule {
    position: absolute;
    height: 2px;
    background: var(--white);
  }
  .rule--left  { top: 399px; left: 63px;  width: 86px; }
  .rule--right { top: 399px; left: 538px; width: 86px; }
  .rule--divider { top: 562px; left: 63px; width: 561px; height: 3px; }
  .address {
    font-size: 39px;
    font-weight: 400;
  }
  .address--street { top: 448px; }
  .address--city   { top: 501px; }
  .agent__name {
    top: 672px;
    font-size: 40px;
    font-weight: 600;
  }
  .agent__title {
    top: 715px;
    font-size: 32px;
    font-weight: 400;
  }
  .contact {
    font-size: 38px;
    font-weight: 400;
  }
  .contact b { font-weight: 700; }
  .contact--phone { top: 779px; }
  .contact--email { top: 826px; }
  .website {
    top: 1130px;
    font-size: 47px;
    font-weight: 700;
    color: var(--navy);
  }
</style>
</head>
<body>
  <main class="card">
    <svg class="card__disc" width="685" height="1200" viewBox="0 0 685 1200" aria-hidden="true">
      <circle cx="343" cy="544" r="521" fill="var(--cyan)"/>
      <circle cx="343" cy="544" r="494" fill="var(--navy)"/>
    </svg>

    <h1 class="line brand__name">Havenrock</h1>
    <span class="rule rule--left"></span>
    <p class="line brand__tagline">REALTY</p>
    <span class="rule rule--right"></span>

    <p class="line address address--street">48391 Cordell Ave., Suite 307</p>
    <p class="line address address--city">Calderon, Texas 78115</p>
    <span class="rule rule--divider"></span>

    <p class="line agent__name">Daniel P Whitcomb III</p>
    <p class="line agent__title">Owner/Broker</p>

    <p class="line contact contact--phone"><b>P</b>:210-555-0147</p>
    <p class="line contact contact--email"><b>E</b>:Daniel@HavenrockTX.com</p>

    <p class="line website">www.HavenrockTX.com</p>
  </main>
</body>
</html>
```